Staff Newsletter Template Image

We are looking for two .jpg images that we can put into a Word document and use for our staff newsletter. We will then add content using text boxes.
Attached is the current template which works for the columns and size that we need but we just want a fresh new design.
The Word document shows how we use it.
The name will stay the same - Team upBeat but can be a different look to the current one.

Target Market(s)

Sales team

Colors

Designer to choose colors to be used in the design.

Requirements
Must have
• Colours will be green, grey and white, possibly cream if needed. All from the guidelines.
• I have attached our brand guidelines which shows design elements and fonts for our brand. Also attached is brand guidelines for one of our product lines as we would like to use the same green.
• It needs to be nice to look at and motivational for our team

```html
<!DOCTYPE html>
<html lang="en">
<head>
<meta charset="utf-8">
<title>Team upBeat – Newsletter Page</title>
<link rel="stylesheet" href="https://fonts.googleapis.com/css2?family=Cabin:wght@400;500&display=swap">
<style>
  :root {
    --paper: #ffffff;
    --charcoal: #3a3a3c;
    --charcoal-deep: #202022;
    --leaf: #8dc43f;
    --leaf-deep: #5a8520;
    --rule: #c8c8c8;
    --ink: #1a1a1a;
    --font-body: "Cabin", "Lato", Arial, sans-serif;
  }
  html, body {
    margin: 0;
    padding: 0;
    overflow: hidden;
    background: var(--paper);
  }
  .page {
    position: relative;
    width: 849px;
    height: 1200px;
    overflow: hidden;
    background: var(--paper);
    font-family: var(--font-body);
  }
  .page__bands {
    position: absolute;
    inset: 0;
    width: 849px;
    height: 1200px;
  }
  .shade--charcoal-base { stop-color: var(--charcoal); }
  .shade--charcoal-edge { stop-color: var(--charcoal-deep); }
  .shade--leaf-base { stop-color: var(--leaf); }
  .shade--leaf-edge { stop-color: var(--leaf-deep); }
  .footer__rule {
    position: absolute;
    left: 412px;
    right: 0;
    top: 1179px;
    height: 1px;
    background: var(--rule);
  }
  .footer__credit,
  .footer__date {
    position: absolute;
    top: 1181px;
    margin: 0;
    font-size: 11px;
    line-height: 14px;
  }
  .footer__credit {
    left: 60px;
    color: var(--paper);
    letter-spacing: 0.01em;
  }
  .footer__date {
    left: 722px;
    font-weight: 500;
    color: var(--ink);
  }
</style>
</head>
<body>
  <main class="page">
    <svg class="page__bands" viewBox="0 0 849 1200" aria-hidden="true">
      <defs>
        <linearGradient id="charcoal-fold" gradientUnits="userSpaceOnUse" x1="728" y1="836" x2="760" y2="870">
          <stop offset="0" class="shade--charcoal-base"/>
          <stop offset="1" class="shade--charcoal-edge"/>
        </linearGradient>
        <linearGradient id="leaf-fold" gradientUnits="userSpaceOnUse" x1="526" y1="1023" x2="560" y2="1059">
          <stop offset="0" class="shade--leaf-base"/>
          <stop offset="1" class="shade--leaf-edge"/>
        </linearGradient>
      </defs>
      <polygon class="band band--charcoal" fill="url(#charcoal-fold)"
               points="651,0 849,0 849,786 672,953 147,466"/>
      <polygon class="band band--leaf" fill="url(#leaf-fold)"
               points="147,466 672,953 410,1200 0,1200 0,601"/>
    </svg>

    <div class="footer__rule"></div>
    <p class="footer__credit">© upBeat Comfort Co.</p>
    <p class="footer__date">Date</p>
  </main>
</body>
</html>
```